Business Card and Letterhead for Copperfield Reed - (Have Logo)

Update 4: Removed company reg no from business card details as it looked a bit out of place. Updated services list.
UPDATE 3
Sorry, I got the address a little bit wrong, have updated it below. Sorry for any inconvenience caused.
UPDATE 2
Finally I have the details for the business cards and letterhead. Submissions already made do not have to be updated unless shortlisted, if all new submissions could include the details for me, Simon, that would be very much appreciated and help with the final shortlist selection. I intend to share a shortlist of the three best entries with past and existing customers for their feedback and opinions. Thank you all again for your time.
Here are the details.
Simon Latchford
Web Developer
T: 01632 418 720
E: simon@copperfieldreed.example
www.copperfieldreed.example
Professional Photography
Web Solutions & E-Commerce
Audio & HD Video Production
Marketing & Promotions
Identity and Branding
Copperfield Reed Ltd
Suite 20938, 3rd Floor
212-224 Marlowe Row
London, EC2R 8KT
Company Reg. No: 09264183
The order and the layout of the information are of course down to the design, but the company registration number should be smaller and less prominent. The formatting of the telephone and email address using a T: and an E: I am not sure about and again if it is Tel: or Email: or Icons is up to the design.
The Company No. on the letterhead should read (somewhere in small text along the bottom):
Copperfield Reed is a Ltd Company registered in England & Wales, Registration No. 09264183.
The second business card details are
Martin Oakley
Photographer
T: 01632 418 720
E: martin@copperfieldreed.example
Everything else the same of course.
Thank you again for all the submissions so far.
END OF UPDATE 2
-
UPDATE 1: Please do not alter the logo nor the logo colours. (This was a previous pixel bazaar project and I am extremely happy with it. The icon can stand alone of course, but I have had to eliminate all entries that have made it black and white, or reversed the icon.) I would like to thank everyone that has participated so far and am very grateful for all your thought and time.
End of Update 1
-
Original Brief:
I have attached the logo vector file.
Following a superb logo from a previous Pixel Bazaar project I am now looking for a business card design and (although less important) a letterhead as well.
I must admit I tried to do it myself but could only come up with the usual amateur stuff that in comparison to the quality of the logo looked awful.
About Us
Copperfield Reed Ltd will be a new company due to start in January. It is really just me (a web developer) and my friend (a photographer). We will be aiming at the usual small to medium sized businesses in the local area, selling various digital services including photographic services to the public, web hosting and development, commercial photography, modelling services (not us!), full video and film production and possibly a bit of marketing as well. (Really it is anything we can do professionally all lumped together! We met running seperate businesses which have both since closed)
We will not be competing on price. We plan to be expensive but fair. Certainly not the cheapest.
What we are looking for
Business Card
I imagine a double sided business card, which will be used for more than one person. I imagine the front to be the same for everyone and the persons details to be on the back, although this is of course only my thoughts and I am of course completely open to any ideas.
The card could also have a services list or a bit about what we do on it. It might feature the website address, our business address (mail forwarding address) or our registered company number.
Or it might have none of that, we are completely open to any ideas and have no real fixed opinions. I just want it to be really nice :-)
Letterhead (secondary importance)
We will make our decision primarily on the business card, although a mathcing letterhead would be fantastic. Something standardish in format and simple, although again, all ideas are welcomed.
I hope that is enough information but if you have any questions I will answer them as fully and as quickly as possible.
Thank you once again and I really look forward to seeing your ideas and picking a winner.
Simon L.
Small businesses AND the general public
Film Production

```html
<!DOCTYPE html>
<html lang="en">
<head>
<meta charset="utf-8">
<title>Copperfield Reed — Letterhead and Business Cards</title>
<link href="https://fonts.googleapis.com/css2?family=Roboto+Condensed:wght@700&family=Open+Sans:wght@400&display=swap" rel="stylesheet">
<style>
  :root {
    --backdrop: #000000;
    --paper: #ffffff;
    --brand-red: #b5121b;
    --card-red: #b0484a;
    --charcoal: #404041;
    --ink: #222222;
    --faint: rgba(255, 255, 255, 0.16);
  }
  * { margin: 0; padding: 0; box-sizing: border-box; }
  html, body {
    width: 1200px;
    height: 1114px;
    overflow: hidden;
    background: var(--backdrop);
  }
  .canvas {
    position: relative;
    width: 1200px;
    height: 1114px;
  }

  /* Wordmark: invented name with a plain square */
  .wordmark {
    position: absolute;
    display: flex;
    align-items: center;
    gap: 10px;
  }
  .wordmark__square {
    display: block;
    background: var(--brand-red);
    flex: none;
  }
  .wordmark__name {
    font-family: "Roboto Condensed", "Arial Narrow", sans-serif;
    font-weight: 700;
    text-transform: uppercase;
    line-height: 0.98;
    letter-spacing: 0.02em;
    color: var(--charcoal);
  }

  /* Letterhead */
  .letterhead {
    position: absolute;
    left: 96px;
    top: 60px;
    width: 730px;
    height: 1034px;
    background: var(--paper);
  }
  .letterhead .wordmark { left: 44px; top: 46px; }
  .letterhead .wordmark__square { width: 48px; height: 48px; }
  .letterhead .wordmark__name { font-size: 25px; }

  .letterhead__accent {
    position: absolute;
    left: 44px;
    top: 852px;
    width: 120px;
    height: 124px;
    background: var(--brand-red);
  }
  .letterhead__base {
    position: absolute;
    left: 44px;
    top: 984px;
    width: 120px;
    height: 50px;
    background: var(--charcoal);
  }
  .letterhead__contact {
    position: absolute;
    top: 988px;
    font-family: "Open Sans", Arial, sans-serif;
    font-size: 12px;
    line-height: 17px;
    color: var(--ink);
    list-style: none;
  }
  .letterhead__contact--left { left: 216px; }
  .letterhead__contact--right { left: 484px; }

  /* Business cards */
  .card {
    position: absolute;
    left: 848px;
    width: 314px;
    border-radius: 10px;
    overflow: hidden;
  }
  .card--front {
    top: 60px;
    height: 182px;
    background: var(--card-red);
  }
  .card__decoration {
    position: absolute;
    left: 196px;
    top: 10px;
    width: 120px;
    height: 120px;
    border: 22px solid var(--faint);
  }
  .card--front .wordmark { left: 20px; top: 64px; }
  .card--front .wordmark__square { width: 44px; height: 44px; background: var(--paper); }
  .card--front .wordmark__name { font-size: 23px; color: var(--paper); }

  .card--back {
    top: 270px;
    height: 180px;
    background: var(--paper);
  }
  .card--back .wordmark { left: 12px; top: 18px; gap: 7px; }
  .card--back .wordmark__square { width: 36px; height: 36px; }
  .card--back .wordmark__name { font-size: 18px; }

  .card__details {
    position: absolute;
    left: 12px;
    font-family: "Open Sans", Arial, sans-serif;
    font-size: 10px;
    line-height: 12.5px;
    color: var(--ink);
    list-style: none;
  }
  .card__details--person { top: 76px; }
  .card__details--contact { top: 114px; }
</style>
</head>
<body>
<main class="canvas">

  <section class="letterhead" aria-label="Letterhead">
    <div class="wordmark">
      <span class="wordmark__square"></span>
      <span class="wordmark__name">Copperfield<br>Reed</span>
    </div>

    <div class="letterhead__accent"></div>
    <div class="letterhead__base"></div>

    <ul class="letterhead__contact letterhead__contact--left">
      <li>Address</li>
      <li>Phone</li>
    </ul>
    <ul class="letterhead__contact letterhead__contact--right">
      <li>Email</li>
      <li>Website</li>
    </ul>
  </section>

  <section class="card card--front" aria-label="Business card front">
    <div class="card__decoration"></div>
    <div class="wordmark">
      <span class="wordmark__square"></span>
      <span class="wordmark__name">Copperfield<br>Reed</span>
    </div>
  </section>

  <section class="card card--back" aria-label="Business card back">
    <div class="wordmark">
      <span class="wordmark__square"></span>
      <span class="wordmark__name">Copperfield<br>Reed</span>
    </div>
    <ul class="card__details card__details--person">
      <li>Name</li>
      <li>Title</li>
    </ul>
    <ul class="card__details card__details--contact">
      <li>Address</li>
      <li>Phone</li>
      <li>Email</li>
      <li>Website</li>
    </ul>
  </section>

</main>
</body>
</html>
```